Do i have coronavirus, flue or cold?

Using information from PFA and government agencies we want to make a easy to read infographic helping patients see if they have coronavirus, the flu or a cold. Using a flow diagram or whatever you think will make it easy to read and digest for the average lamen.

Information is in the word document and in the chart.

We are www.calvexa.co.uk attached is our brand guidelines, we will be putting this infographic on our website and email/sms it to all of our 300,000 patients.

```html
<!DOCTYPE html>
<html lang="en">
<head>
<meta charset="UTF-8">
<title>Coronavirus, flu or cold? – Calvexa</title>
<link rel="stylesheet" href="https://fonts.googleapis.com/css2?family=Arimo:wght@400;700&display=swap">
<style>
  :root {
    --ink: #3338b8;
    --brand-light: #6f8ff3;
    --symptom-cell: #ffa07d;
    --covid-cell: #ff693e;
    --other-cell: #d3dbf2;
    --panel: #ecf4f5;
    --rule: #5a5a6a;
    --page: #ffffff;
  }
  * { box-sizing: border-box; margin: 0; padding: 0; }
  html, body { width: 1200px; height: 890px; overflow: hidden; background: var(--page); }
  .poster {
    position: relative;
    width: 1200px;
    height: 890px;
    border: 1px solid #444;
    font-family: "Arimo", Arial, sans-serif;
    color: var(--ink);
    background: var(--page);
  }
  .brand {
    position: absolute;
    left: 16px;
    top: 30px;
    display: flex;
    align-items: center;
    gap: 12px;
  }
  .brand-dot {
    width: 62px;
    height: 62px;
    border-radius: 50%;
    background: var(--ink);
  }
  .brand-name {
    font-size: 40px;
    font-weight: 700;
    color: var(--ink);
    letter-spacing: -0.5px;
  }
  .heading {
    position: absolute;
    left: 430px;
    width: 650px;
    top: 8px;
    text-align: center;
  }
  .heading-title {
    font-size: 44px;
    font-weight: 700;
    line-height: 1.05;
  }
  .heading-sub {
    font-size: 28px;
    font-weight: 400;
    line-height: 1.1;
  }
  .illustration {
    position: absolute;
    left: 22px;
    top: 290px;
    width: 265px;
    height: 590px;
  }
  .panel {
    position: absolute;
    left: 317px;
    top: 84px;
    width: 854px;
    height: 780px;
    background: var(--panel);
    border-radius: 8px;
  }
  .symptom-table {
    position: absolute;
    left: 350px;
    top: 104px;
    width: 789px;
    height: 735px;
    border-collapse: collapse;
    table-layout: fixed;
    text-align: center;
  }
  .symptom-table th,
  .symptom-table td {
    border: 1px solid var(--rule);
    font-weight: 700;
    color: var(--ink);
    vertical-align: middle;
    line-height: 1.12;
  }
  .symptom-table thead th {
    background: var(--brand-light);
    height: 67px;
    font-size: 22px;
    padding-top: 6px;
  }
  .symptom-table tbody td { height: 66.8px; font-size: 27px; }
  .symptom-table .col-symptom { background: var(--symptom-cell); }
  .symptom-table .col-covid { background: var(--covid-cell); }
  .symptom-table .col-other { background: var(--other-cell); }
</style>
</head>
<body>
<div class="poster">
  <div class="brand">
    <span class="brand-dot"></span>
    <span class="brand-name">Calvexa</span>
  </div>

  <header class="heading">
    <h1 class="heading-title">Coronavirus, flu or cold?</h1>
    <p class="heading-sub">Learn how to tell the difference</p>
  </header>

  <svg class="illustration" role="img" aria-label="Illustration of a doctor in a white coat with a stethoscope, holding a blue clipboard" viewBox="0 0 265 590">
    <defs>
      <linearGradient id="doctorTone" x1="0" y1="0" x2="0" y2="1">
        <stop offset="0" stop-color="#d3dbf2"/>
        <stop offset="0.55" stop-color="#c7d0ef"/>
        <stop offset="1" stop-color="#3344b8"/>
      </linearGradient>
    </defs>
    <rect x="0" y="0" width="265" height="590" rx="14" fill="url(#doctorTone)"/>
  </svg>

  <div class="panel"></div>

  <table class="symptom-table">
    <thead>
      <tr>
        <th>SYMPTOMS</th>
        <th>CORONAVIRUS<br>COVID-19</th>
        <th>FLU</th>
        <th>COLD</th>
      </tr>
    </thead>
    <tbody>
      <tr><td class="col-symptom">Fever</td><td class="col-covid">Yes</td><td class="col-other">Yes</td><td class="col-other">Rare</td></tr>
      <tr><td class="col-symptom">Cough</td><td class="col-covid">Yes</td><td class="col-other">Yes</td><td class="col-other">Moderate</td></tr>
      <tr><td class="col-symptom">Tiredness</td><td class="col-covid">Yes</td><td class="col-other">Yes</td><td class="col-other">Moderate</td></tr>
      <tr><td class="col-symptom">Shortness<br>of breath</td><td class="col-covid">Yes</td><td class="col-other">Yes</td><td class="col-other">Rare</td></tr>
      <tr><td class="col-symptom">Muscle<br>aches</td><td class="col-covid">Yes</td><td class="col-other">Yes</td><td class="col-other">Moderate</td></tr>
      <tr><td class="col-symptom">Headache</td><td class="col-covid">Sometimes</td><td class="col-other">Yes</td><td class="col-other">Rare</td></tr>
      <tr><td class="col-symptom">Sore<br>throat</td><td class="col-covid">Sometimes</td><td class="col-other">Sometimes</td><td class="col-other">Yes</td></tr>
      <tr><td class="col-symptom">Runny or<br>stuffy nose</td><td class="col-covid">Rare</td><td class="col-other">Sometimes</td><td class="col-other">Yes</td></tr>
      <tr><td class="col-symptom">Sneezing</td><td class="col-covid">No</td><td class="col-other">Sometimes</td><td class="col-other">Yes</td></tr>
      <tr><td class="col-symptom">Diarrhorea</td><td class="col-covid">Rare</td><td class="col-other">Sometimes</td><td class="col-other">No</td></tr>
    </tbody>
  </table>
</div>
</body>
</html>
```